Business Card design for new private practice opening

I need a business card design for my new private practice with my new logo uploaded as a file
On the front the logo
On the back: maybe a small logo somewhere?
Priv. Doz. DDr. Corinna Vestaluk
Fachärztin für Allgemein- & Viszeralchirurgie
Address: xxx
Tel: xxx
Mobil:xxx
Webseite:xxx
Email:xxx

Contact Information for Business Card

See project description above for details

Requirements
Nice to have
• I would like the colors of the logo incorporated into the business card

```html
<!DOCTYPE html>
<html lang="de">
<head>
<meta charset="utf-8">
<title>Visitenkarte – Vestaluk Chirurgie</title>
<link rel="stylesheet" href="https://fonts.googleapis.com/css2?family=Montserrat:wght@700&family=Mulish:wght@400;600;700&display=swap">
<style>
  :root {
    --backdrop: #000c3d;
    --card: #ffffff;
    --teal: #2fa8a8;
    --teal-text: #26999c;
    --grey: #7c7c7c;
    --grey-text: #6b6b6b;
    --icon: #707070;
  }
  * { margin: 0; padding: 0; box-sizing: border-box; }
  html, body {
    width: 1200px; height: 1200px; overflow: hidden;
    background: var(--backdrop);
  }
  .canvas { position: relative; width: 1200px; height: 1200px; }

  .card {
    position: absolute;
    background: var(--card);
    border-radius: 15px;
    overflow: hidden;
  }

  /* Front */
  .card-front { left: 148px; top: 121px; width: 918px; height: 442px; }
  .front-mark {
    position: absolute; left: 182px; top: 120px;
    width: 200px; height: 200px; border-radius: 50%;
    background: var(--teal);
  }
  .front-name {
    position: absolute; left: 405px; top: 148px;
    font-family: "Montserrat", sans-serif; font-weight: 700;
    font-size: 61px; line-height: 70px; letter-spacing: 1px;
    color: var(--grey);
  }

  /* Back */
  .card-back { left: 144px; top: 616px; width: 921px; height: 462px; }
  .back-mark {
    position: absolute; left: 52px; top: 22px;
    width: 134px; height: 134px; border-radius: 50%;
    background: var(--teal);
  }
  .holder-name {
    position: absolute; left: 219px; top: 42px;
    font-family: "Mulish", sans-serif; font-weight: 700;
    font-size: 39px; color: var(--grey); white-space: nowrap;
  }
  .holder-title {
    position: absolute; left: 219px; top: 100px;
    font-family: "Mulish", sans-serif; font-weight: 400;
    font-size: 28.5px; color: var(--teal-text); white-space: nowrap;
  }
  .divider {
    position: absolute; left: 50px; top: 175px;
    width: 818px; height: 3px; background: var(--teal);
  }
  .contact {
    position: absolute; display: flex; align-items: center;
    font-family: "Mulish", sans-serif; font-weight: 400;
    font-size: 27px; color: var(--grey-text); white-space: nowrap;
    height: 40px;
  }
  .contact svg { width: 30px; height: 30px; margin-right: 16px; fill: var(--icon); flex: none; }
  .col-left { left: 60px; }
  .col-right { left: 506px; }
  .row-1 { top: 212px; }
  .row-2 { top: 264px; }
  .row-3 { top: 316px; }
  .row-4 { top: 368px; }
  .bottom-band {
    position: absolute; left: 0; bottom: 0;
    width: 100%; height: 12px; background: var(--teal);
  }
</style>
</head>
<body>
<div class="canvas">

  <section class="card card-front">
    <div class="front-mark"></div>
    <div class="front-name">VESTALUK<br>CHIRURGIE</div>
  </section>

  <section class="card card-back">
    <div class="back-mark"></div>
    <div class="holder-name">Priv. Doz. DDr. Corinna Vestaluk</div>
    <div class="holder-title">Fachärztin für Allgemein- &amp; Viszeralchirurgie</div>
    <div class="divider"></div>

    <div class="contact col-left row-1">
      <svg viewBox="0 0 24 24"><path d="M12 2a7 7 0 0 0-7 7c0 5 7 13 7 13s7-8 7-13a7 7 0 0 0-7-7zm0 9.5A2.5 2.5 0 1 1 12 6.5a2.5 2.5 0 0 1 0 5z"/></svg>
      Address: xxx
    </div>
    <div class="contact col-left row-2">
      <svg viewBox="0 0 24 24"><path d="M6.6 10.8a15.1 15.1 0 0 0 6.6 6.6l2.2-2.2a1 1 0 0 1 1-.25 11.4 11.4 0 0 0 3.6.57 1 1 0 0 1 1 1V20a1 1 0 0 1-1 1A17 17 0 0 1 3 4a1 1 0 0 1 1-1h3.5a1 1 0 0 1 1 1c0 1.25.2 2.45.57 3.57a1 1 0 0 1-.25 1z"/></svg>
      Tel: xxx
    </div>
    <div class="contact col-left row-3">
      <svg viewBox="0 0 24 24"><path d="M7 2h10a2 2 0 0 1 2 2v16a2 2 0 0 1-2 2H7a2 2 0 0 1-2-2V4a2 2 0 0 1 2-2zm0 2v14h10V4zm4 15.2v1h2v-1z"/></svg>
      Mobil: xxx
    </div>
    <div class="contact col-left row-4">
      <svg viewBox="0 0 24 24"><path d="M2 5h20v14H2zm2 2v.4l8 5.3 8-5.3V7z"/></svg>
      Email: xxx
    </div>
    <div class="contact col-right row-3">
      <svg viewBox="0 0 24 24" fill="none" stroke="#707070" stroke-width="1.6"><circle cx="12" cy="12" r="9.5"/><ellipse cx="12" cy="12" rx="4.2" ry="9.5"/><path d="M2.5 12h19M4 7h16M4 17h16"/></svg>
      Website: xxx
    </div>
    <div class="contact col-right row-4">
      <svg viewBox="0 0 24 24"><path d="M2 5h20v14H2zm2 2v.4l8 5.3 8-5.3V7z"/></svg>
      Email: xxx
    </div>

    <div class="bottom-band"></div>
  </section>

</div>
</body>
</html>
```